Solmira Coast Island Weddings, Inc.

Solmira Coast Island Weddings Business Card design for Cardovelle. Clean, contemporary, creative, colorful (using colors provided). ONE SIDE SHOULD INCLUDE logo, www.solmiracoastweddings.com, @vowsbythecove. OTHER SIDE SHOULD INCLUDE Marisol Tennant. Owner & Officiant. Marbella Cove, Solmira. 555.407.1892. marisol@solmiracoastweddings.com. Colors are blue #58AA9E
and golden #e2bf80)

Target Market(s)

Destination Wedding Clients in the United States

Contact Information for Business Card

Marisol Tennant
Owner & Officiant
Marbella Cove, Solmira
555.407.1892
marisol@solmiracoastweddings.com

Font styles to use
Sans Serif

Requirements
Must have
• Colorful (colors are blue #58AA9E
• and golden #e2bf80), clean, contemporary. ONE SIDE SHOULD INCLUDE logo, www.solmiracoastweddings.com, @vowsbythecove. Other side should include Marisol Tennant. Owner & Officiant. Marbella Cove, Solmira. 555.407.1892. marisol@solmiracoastweddings.com
Nice to have
• I would like to see a version that includes my bio photo, and one that doesn't include the bio photo

```html
<!DOCTYPE html>
<html lang="en">
<head>
<meta charset="utf-8">
<title>Solmira Coast Island Weddings – Business Card</title>
<link rel="stylesheet" href="https://fonts.googleapis.com/css2?family=Roboto:wght@300;400;700&family=Roboto+Condensed:wght@400;700&display=swap">
<style>
  :root {
    --teal: #58aa9e;
    --gold: #e2bf80;
    --gold-deep: #d8b771;
    --paper: #f4f4f3;
    --ink: #4a4a4a;
    --backdrop: #2a2a2a;
    --rule: #bdbdbd;
  }
  * { margin: 0; padding: 0; box-sizing: border-box; }
  html, body { width: 1200px; height: 960px; overflow: hidden; }
  body {
    position: relative;
    background: var(--backdrop);
    font-family: "Roboto", Arial, sans-serif;
  }
  .card {
    position: absolute;
    width: 600px;
    height: 342px;
    border-radius: 22px;
    overflow: hidden;
  }
  .card--front { left: 302px; top: 124px; background: var(--paper); }
  .card--back  { left: 299px; top: 493px; background: var(--gold-deep); }

  .front-stripe {
    position: absolute; left: 0; right: 0; bottom: 0; height: 16px;
    background: var(--gold);
    border-top: 3px solid var(--teal);
  }

  .brand {
    position: absolute;
    text-align: center;
    font-weight: 300;
  }
  .brand__mark {
    display: block;
    margin: 0 auto;
    border-radius: 50%;
  }
  .brand__name { display: block; }
  .brand__tagline { display: block; text-transform: uppercase; }

  .card--front .brand { left: 40px; width: 246px; top: 100px; color: var(--gold); }
  .card--front .brand__mark { width: 50px; height: 50px; border: 2px solid var(--gold); margin-bottom: 20px; }
  .card--front .brand__name { font-size: 31px; line-height: 1; letter-spacing: 0.5px; }
  .card--front .brand__tagline { font-size: 11px; letter-spacing: 2.6px; margin-top: 10px; }

  .divider {
    position: absolute; left: 299px; top: 94px; width: 1px; height: 158px;
    background: var(--rule);
  }

  .contact { position: absolute; left: 320px; top: 94px; }
  .contact__name {
    font-family: "Roboto Condensed", Arial, sans-serif;
    font-weight: 700; font-size: 21px; color: var(--teal);
    text-transform: uppercase; line-height: 1.05;
  }
  .contact__role {
    font-family: "Roboto Condensed", Arial, sans-serif;
    font-weight: 700; font-size: 15.5px; color: var(--gold);
    text-transform: uppercase; line-height: 1.2;
  }
  .contact__place { font-size: 14.5px; color: var(--ink); margin-top: 8px; }
  .contact__list { list-style: none; margin-top: 9px; }
  .contact__item {
    display: flex; align-items: center; gap: 8px;
    font-size: 14.5px; color: var(--ink); height: 19.5px;
  }
  .contact__item--email { font-family: "Roboto Condensed", Arial, sans-serif; font-size: 14.5px; }
  .contact__icon { width: 13px; height: 13px; flex: none; fill: var(--teal); }

  .card--back .brand { left: 0; right: 0; top: 80px; color: #fff; }
  .card--back .brand__mark { width: 62px; height: 62px; border: 2px solid #fff; margin-bottom: 22px; }
  .card--back .brand__name { font-size: 40px; line-height: 1; letter-spacing: 0.5px; }
  .card--back .brand__tagline { font-size: 13px; letter-spacing: 3px; margin-top: 12px; }

  .back-url {
    position: absolute; left: 0; right: 0; top: 297px;
    text-align: center; color: #fff;
    font-size: 14px; letter-spacing: 3px;
  }
</style>
</head>
<body>

<section class="card card--front">
  <div class="brand">
    <span class="brand__mark"></span>
    <span class="brand__name">solmira coast</span>
    <span class="brand__tagline">Island Weddings</span>
  </div>

  <div class="divider"></div>

  <div class="contact">
    <p class="contact__name">Marisol Tennant</p>
    <p class="contact__role">Owner &amp; Officiant</p>
    <p class="contact__place">Marbella Cove, Solmira</p>
    <ul class="contact__list">
      <li class="contact__item">
        <svg class="contact__icon" viewBox="0 0 16 16"><path d="M3.6 1.2l2.2 2.6c.3.4.3.9 0 1.3L4.7 6.3c.8 2 2.5 3.8 4.9 5l1.2-1.1c.4-.3.9-.3 1.3 0l2.6 2.2c.4.4.4 1 0 1.3l-1.4 1.4C10.5 16.4 0 6.6 1 2.6L2.3 1.2c.4-.4.9-.4 1.3 0z"/></svg>
        555.407.1892
      </li>
      <li class="contact__item contact__item--email">
        <svg class="contact__icon" viewBox="0 0 16 16"><path d="M1 3h14v1.2L8 8.8 1 4.2z"/><path d="M1 5.6l7 4.6 7-4.6V13H1z"/></svg>
        marisol@solmiracoastweddings.com
      </li>
      <li class="contact__item">
        <svg class="contact__icon" viewBox="0 0 16 16"><circle cx="8" cy="8" r="6.5" fill="none" stroke="#58aa9e" stroke-width="1.6"/><path d="M4 4.5c1.5.5 2.5 0 3.5 1.5s-1 2 0 3.5 2 1 2 3" fill="none" stroke="#58aa9e" stroke-width="1.6"/></svg>
        solmiracoastweddings.com
      </li>
      <li class="contact__item">
        <svg class="contact__icon" viewBox="0 0 16 16"><circle cx="8" cy="8" r="6.5"/></svg>
        @vowsbythecove
      </li>
    </ul>
  </div>

  <div class="front-stripe"></div>
</section>

<section class="card card--back">
  <div class="brand">
    <span class="brand__mark"></span>
    <span class="brand__name">solmira coast</span>
    <span class="brand__tagline">Island Weddings</span>
  </div>
  <p class="back-url">www.solmiracoastweddings.com</p>
</section>

</body>
</html>
```